Onboarding Carousel UI/UX design

We need a great UI/UX design for our onboarding carousel as attached in the PDF document. The chosen designers will be given our brand book with colors and styles to be used. The images must be focused on the content of each slide and be professional unique style (Do not use the childish cartoons we have used for placeholders)

Industry/Entity Type

Mortgage Brokerage

Number of Pages Required

5+ page

Other font styles liked:
• Roboto

Requirements
Must have
• Great UI / UX design
Very relevant content of the images to match the slide
Nice to have
• Brand book

https://proto.velmarink.com/view/a4c7e210-8b3f-4d19-a6e2-5f0c91b7d3e8-c2fa/?fullscreen

Image styles we like. Would need to be customized and made unique for us.

https://pixelmarsh.com/shots/4817302-Tarvo-Quillnet-Illustration-Collaboration
https://brackwellstudio.co.za/software-client-style-frames
Should not have
• Do not use the childish images we have used as placeholders

```html
<!DOCTYPE html>
<html lang="en">
<head>
<meta charset="utf-8">
<title>Onboarding Carousel</title>
<link href="https://fonts.googleapis.com/css2?family=Roboto:ital,wght@0,400;0,500;0,700;1,400&display=swap" rel="stylesheet">
<style>
  :root {
    --navy: #0b2450;
    --title: #0f2a5c;
    --backdrop: #9a9a9a;
    --crimson: #a6004e;
    --footer: #eceef2;
    --text: #1f1f1f;
    --muted: #6b6b6b;
    --link: #1c4fa0;
    --dot: #8d8d8d;
  }
  * { box-sizing: border-box; margin: 0; padding: 0; }
  html, body { width: 1200px; height: 4236px; overflow: hidden; }
  body { font-family: 'Roboto', sans-serif; background: var(--backdrop); position: relative; }
  .backdrop { position: absolute; inset: 0; width: 1200px; height: 4236px; }

  .screen {
    position: absolute; width: 452px; height: 986px;
    background: #fff; display: flex; flex-direction: column;
    box-shadow: 0 4px 18px rgba(0,0,0,.25);
  }
  .col-a { left: 128px; } .col-b { left: 618px; }
  .row-1 { top: 89px; } .row-2 { top: 1113px; } .row-3 { top: 2136px; } .row-4 { top: 3158px; }

  .screen-body { height: 816px; display: flex; flex-direction: column; align-items: center; padding: 14px 20px 0; text-align: center; }
  .illustration { border-radius: 14px; flex: none; }
  .slide-title { color: var(--title); font-weight: 500; font-size: 47px; line-height: 57px; margin-top: 18px; }
  .slide-lead { color: var(--text); font-size: 29px; line-height: 45px; margin-top: 20px; max-width: 395px; }
  .slide-note { color: var(--muted); font-size: 22px; line-height: 36px; margin-top: 22px; max-width: 395px; }

  .dots { display: flex; gap: 13px; margin-top: auto; margin-bottom: 40px; }
  .dot { width: 12px; height: 12px; border-radius: 50%; border: 2px solid var(--dot); }
  .dot.active { background: var(--dot); }

  .screen-footer { height: 109px; background: var(--footer); display: flex; align-items: center; justify-content: center; padding: 0 25px; }
  .screen-footer.split { justify-content: space-between; }
  .login-hint { font-size: 17px; font-style: italic; color: var(--text); line-height: 26px; }
  .login-hint a { display: block; font-style: normal; font-size: 24px; color: var(--link); text-decoration: underline; }
  .btn {
    background: var(--crimson); color: #fff; font-weight: 700; font-size: 20px;
    height: 60px; min-width: 140px; padding: 0 34px; border-radius: 30px;
    display: flex; align-items: center; justify-content: center; letter-spacing: .2px;
  }
  .nav-bar { height: 61px; background: var(--navy); display: flex; align-items: center; justify-content: center; gap: 70px; }

  .feature { position: relative; width: 100%; height: 230px; text-align: left; }
  .feature h3 { color: var(--title); font-weight: 500; font-size: 29px; line-height: 35px; }
  .feature p { color: var(--text); font-size: 20px; line-height: 32px; margin-top: 12px; width: 205px; }
  .feature .copy { position: absolute; top: 0; }
  .feature .illustration { position: absolute; }
</style>
</head>
<body>

<svg class="backdrop" viewBox="0 0 1200 4236" aria-hidden="true">
  <path d="M0 0 H1200 V330 C900 520 420 230 0 400 Z" fill="#0b2450"/>
  <path d="M0 3520 C300 3440 700 3440 1200 3430 V4236 H0 Z" fill="#0b2450"/>
</svg>

<!-- Welcome -->
<section class="screen col-a row-1">
  <div class="screen-body">
    <div class="illustration" role="img" aria-label="Illustration of a street of houses with rent and sale signs" style="width:400px;height:190px;background:linear-gradient(180deg,#d6eef3,#f3e3e6);"></div>
    <h1 class="slide-title">Welcome to Larkhaven Brokers Apply Online</h1>
    <p class="slide-lead" style="max-width:380px;">You can apply online for your next mortgage credit in about 20 minutes.</p>
    <p class="slide-note" style="max-width:385px;">It’s easy, and we will guide you all the way.See the five simple steps that you have to take!</p>
    <div class="dots"><span class="dot active"></span><span class="dot"></span><span class="dot"></span><span class="dot"></span><span class="dot"></span><span class="dot"></span><span class="dot"></span></div>
  </div>
  <div class="screen-footer split">
    <div class="login-hint">Already have an account?<a>Logon</a></div>
    <div class="btn">NEXT</div>
  </div>
  <nav class="nav-bar">
    <svg width="24" height="22" viewBox="0 0 24 22"><path d="M0 2h24M0 11h24M0 20h24" stroke="#fff" stroke-width="3"/></svg>
    <svg width="22" height="22"><rect width="22" height="22" rx="2" fill="#fff"/></svg>
    <svg width="16" height="22"><path d="M16 0 V22 L0 11 Z" fill="#fff"/></svg>
  </nav>
</section>

<!-- #4 -->
<section class="screen col-b row-1">
  <div class="screen-body">
    <div class="illustration" role="img" aria-label="Illustration of a person on a computer screen with profile forms and a padlock" style="width:300px;height:220px;background:linear-gradient(180deg,#d9eef6,#fde6c8);"></div>
    <h2 class="slide-title">#4 Create your profile data for the application</h2>
    <p class="slide-lead" style="line-height:38px;max-width:355px;">Tell us about your current situation including employment, income, assets and liabilities</p>
    <p class="slide-note" style="max-width:370px;">It is essential to have everything as accurate as possible so you can be presented with the right offers.</p>
    <div class="dots"><span class="dot"></span><span class="dot"></span><span class="dot"></span><span class="dot"></span><span class="dot active"></span><span class="dot"></span><span class="dot"></span></div>
  </div>
  <div class="screen-footer"><div class="btn">NEXT</div></div>
  <nav class="nav-bar">
    <svg width="24" height="22" viewBox="0 0 24 22"><path d="M0 2h24M0 11h24M0 20h24" stroke="#fff" stroke-width="3"/></svg>
    <svg width="22" height="22"><rect width="22" height="22" rx="2" fill="#fff"/></svg>
    <svg width="16" height="22"><path d="M16 0 V22 L0 11 Z" fill="#fff"/></svg>
  </nav>
</section>

<!-- #1 -->
<section class="screen col-a row-2">
  <div class="screen-body">
    <div class="illustration" role="img" aria-label="Illustration of a hand holding a phone with an account form and an email envelope" style="width:270px;height:280px;background:linear-gradient(180deg,#dff3f6,#fbe7c4);"></div>
    <h2 class="slide-title">#1 Create your personal account</h2>
    <p class="slide-lead" style="max-width:370px;">You will need a valid email address to create your account</p>
    <p class="slide-note">We will send you a confirmation email, make sure you click the link to verify your email address.</p>
    <div class="dots"><span class="dot"></span><span class="dot active"></span><span class="dot"></span><span class="dot"></span><span class="dot"></span><span class="dot"></span><span class="dot"></span></div>
  </div>
  <div class="screen-footer"><div class="btn">NEXT</div></div>
  <nav class="nav-bar">
    <svg width="24" height="22" viewBox="0 0 24 22"><path d="M0 2h24M0 11h24M0 20h24" stroke="#fff" stroke-width="3"/></svg>
    <svg width="22" height="22"><rect width="22" height="22" rx="2" fill="#fff"/></svg>
    <svg width="16" height="22"><path d="M16 0 V22 L0 11 Z" fill="#fff"/></svg>
  </nav>
</section>

<!-- Features -->
<section class="screen col-b row-2">
  <div class="screen-body" style="padding:24px 0 0 0;">
    <div class="feature">
      <div class="copy" style="left:33px;width:230px;">
        <h3>Our service<br>is 100% free</h3>
        <p>The banks pay us a commission, so you don’t have too</p>
      </div>
      <div class="illustration" role="img" aria-label="Illustration of a hand holding a phone showing a tick" style="right:48px;top:0;width:120px;height:200px;background:linear-gradient(180deg,#eef7f1,#e4e7ec);"></div>
    </div>
    <div class="feature" style="margin-top:8px;">
      <div class="illustration" role="img" aria-label="Illustration of a team of advisers meeting at a table" style="left:10px;top:10px;width:160px;height:130px;background:linear-gradient(180deg,#dcecf7,#e8eaee);"></div>
      <div class="copy" style="left:206px;width:240px;">
        <h3>Team of experts here to help yo</h3>
        <p>The banks pay us a commission, so you don’t have too</p>
      </div>
    </div>
    <div class="feature" style="margin-top:30px;">
      <div class="copy" style="left:33px;width:260px;">
        <h3>Made in Romania<br>with love</h3>
        <p>We love to help people and would love to have you as our customer</p>
      </div>
      <div class="illustration" role="img" aria-label="Decorative pair of red outlined hearts" style="right:0;top:45px;width:180px;height:120px;background:linear-gradient(90deg,#ffffff,#f8d9de);border-radius:14px 0 0 14px;"></div>
    </div>
    <div class="dots"><span class="dot"></span><span class="dot"></span><span class="dot"></span><span class="dot"></span><span class="dot"></span><span class="dot"></span><span class="dot active"></span></div>
  </div>
  <div class="screen-footer"><div class="btn">GET STARTED</div></div>
  <nav class="nav-bar">
    <svg width="24" height="22" viewBox="0 0 24 22"><path d="M0 2h24M0 11h24M0 20h24" stroke="#fff" stroke-width="3"/></svg>
    <svg width="22" height="22"><rect width="22" height="22" rx="2" fill="#fff"/></svg>
    <svg width="16" height="22"><path d="M16 0 V22 L0 11 Z" fill="#fff"/></svg>
  </nav>
</section>

<!-- #2 -->
<section class="screen col-a row-3">
  <div class="screen-body">
    <div class="illustration" role="img" aria-label="Illustration of a hand holding a key in front of a security shield" style="width:260px;height:255px;background:radial-gradient(circle,#8fd0f7,#e3f3fd);border-radius:50%;"></div>
    <h2 class="slide-title" style="margin-top:24px;">#2 Secure your account with your mobile phone</h2>
    <p class="slide-lead" style="margin-top:14px;">You will need a valid mobile phone number to enable two factor authentication.</p>
    <p class="slide-note" style="max-width:375px;">We will send you an SMS containing a security code to verify your mobile number.</p>
    <div class="dots"><span class="dot"></span><span class="dot"></span><span class="dot active"></span><span class="dot"></span><span class="dot"></span><span class="dot"></span><span class="dot"></span></div>
  </div>
  <div class="screen-footer"><div class="btn">NEXT</div></div>
  <nav class="nav-bar">
    <svg width="24" height="22" viewBox="0 0 24 22"><path d="M0 2h24M0 11h24M0 20h24" stroke="#fff" stroke-width="3"/></svg>
    <svg width="22" height="22"><rect width="22" height="22" rx="2" fill="#fff"/></svg>
    <svg width="16" height="22"><path d="M16 0 V22 L0 11 Z" fill="#fff"/></svg>
  </nav>
</section>

<!-- #5 -->
<section class="screen col-b row-3">
  <div class="screen-body">
    <div class="illustration" role="img" aria-label="Illustration of a house surrounded by finance and lifestyle icons" style="width:340px;height:260px;background:radial-gradient(circle,#e6f2fb,#ffffff);"></div>
    <h2 class="slide-title" style="margin-top:10px;line-height:52px;">#5 Apply for the right loan for your needs</h2>
    <p class="slide-lead" style="margin-top:12px;line-height:39px;max-width:360px;">You will be presented with your options,upload any supporting documents and then submit your application online.</p>
    <p class="slide-note" style="max-width:340px;">Then we take it from here to get your approval.</p>
    <div class="dots"><span class="dot"></span><span class="dot"></span><span class="dot"></span><span class="dot"></span><span class="dot"></span><span class="dot active"></span><span class="dot"></span></div>
  </div>
  <div class="screen-footer"><div class="btn">NEXT</div></div>
  <nav class="nav-bar">
    <svg width="24" height="22" viewBox="0 0 24 22"><path d="M0 2h24M0 11h24M0 20h24" stroke="#fff" stroke-width="3"/></svg>
    <svg width="22" height="22"><rect width="22" height="22" rx="2" fill="#fff"/></svg>
    <svg width="16" height="22"><path d="M16 0 V22 L0 11 Z" fill="#fff"/></svg>
  </nav>
</section>

<!-- #3 -->
<section class="screen col-a row-4">
  <div class="screen-body">
    <div class="illustration" role="img" aria-label="Illustration of a phone confirming a verified identity with signal waves" style="width:270px;height:250px;background:linear-gradient(180deg,#8fd0f7,#4aa8ee);"></div>
    <h2 class="slide-title" style="margin-top:22px;">#3 Verify your identity online</h2>
    <p class="slide-lead">You will need to have a valid Romanian ID card or residence permit</p>
    <p class="slide-note" style="max-width:340px;">From your smart phone, you will take a photo of your card and make a selfie video.</p>
    <div class="dots"><span class="dot"></span><span class="dot"></span><span class="dot"></span><span class="dot active"></span><span class="dot"></span><span class="dot"></span><span class="dot"></span></div>
  </div>
  <div class="screen-footer"><div class="btn">NEXT</div></div>
  <nav class="nav-bar">
    <svg width="24" height="22" viewBox="0 0 24 22"><path d="M0 2h24M0 11h24M0 20h24" stroke="#fff" stroke-width="3"/></svg>
    <svg width="22" height="22"><rect width="22" height="22" rx="2" fill="#fff"/></svg>
    <svg width="16" height="22"><path d="M16 0 V22 L0 11 Z" fill="#fff"/></svg>
  </nav>
</section>

</body>
</html>
```